Oxford Choir needs a concert poster!

22nd November is St Wendelin's Day, the Patron Saint of music. 100 years ago on that day, Rupert Calloway was born, famously dubbed the "greatest English composer since Marlowe". 50 years ago that day, three of the most prominent men in history died: this trifecta included theologian and author of 'Quelmor' R. P. Dunmore, philosopher and author of 'Silent Amber Shore' Peregrine Vostell, and one of America's most beloved presidents, Walter P. Hargrove.

In memory of these prominent figures of the 20th century, the Choir of St Oswin by the Tanner Row (the Parish Kirk of Fenwold) perform some of the world's best vocal music composed or inspired by these men. The playlist includes Calloway's 'Canticle for St Wendelin', G. F. Olbrich's 'Sieh, Vater, sieh', 'The Orchard' by Peregrine Vostell set to music by Percy Madden, and Clement Yardley' 'Hold her, sea, in quiet keeping', written specially for the memorial service of President Walter P Hargrove in Marlbury Grand Minster.

We are looking for a dramatic concert poster / or series of posters that encapsulate all these important aspects on this one day. Tickets will be set up on passgrabber.example - space for their logo will be needed.

22nd November 2013, 8pm
Radley Hall Oratory, Oxford
Choir of St Oswin by the Tanner Row
Giles Pemberton-Roe
Tickets: £5

Mostly students and staff from the Universities of Oxford and Whitfield, but also singers from local Oxfordshire choral societies who have a passion for singing and the repertoire. Local musical professionals and appreciators. Not really suitable for children. Cultured adults that support local artistic projects and go to live classical concerts. Higher-end readership. I would like to charge much more for the ticket prices (in order to reflect the quality of the performance) but Oxford is haemorrhaging quality concerts for very little, and the competition is fierce. This poster needs to stand out from the crowd of other events going on, and perhaps be coupled with an inventive marketing strategy.

• St Oswin by the Tanner Row logo
Passgrabber.example logo

My name prominently displayed

```html
<!DOCTYPE html>
<html lang="en">
<head>
<meta charset="utf-8">
<title>St Wendelin's Day – Concert Poster</title>
<link rel="stylesheet" href="https://fonts.googleapis.com/css2?family=Pinyon+Script&family=Cormorant+Garamond:wght@700&family=Sorts+Mill+Goudy&display=swap">
<style>
  :root {
    --page: #ffffff;
    --night: #1a1918;
    --stone: #4a4642;
    --stone-dark: #2a2826;
    --score: #8a7a68;
    --peach: #f3c49a;
    --peach-deep: #d99a68;
    --ink: #1a120b;
    --wood-light: #c98a4e;
    --wood-mid: #9a5f2c;
    --wood-dark: #3a200c;
  }
  * { margin: 0; padding: 0; box-sizing: border-box; }
  html, body {
    width: 1200px; height: 900px; overflow: hidden;
    background: var(--page);
  }
  .poster {
    position: absolute; left: 320px; top: 82px;
    width: 561px; height: 735px; overflow: hidden;
    background: var(--night);
  }
  .building {
    position: absolute; inset: 0 0 auto 0; height: 500px;
    background:
      linear-gradient(90deg, rgba(20,19,18,.6) 0%, rgba(20,19,18,0) 30%, rgba(20,19,18,0) 70%, rgba(20,19,18,.5) 100%),
      linear-gradient(180deg, var(--stone-dark) 0%, var(--stone) 30%, #3b3835 65%, #141312 100%);
  }
  .score {
    position: absolute; left: 0; right: 0; top: 0; height: 170px;
    background: linear-gradient(180deg, rgba(138,122,104,.28) 0%, rgba(138,122,104,.12) 60%, rgba(138,122,104,0) 100%);
  }
  .floor {
    position: absolute; left: 0; right: 0; bottom: 0; height: 250px;
    background:
      radial-gradient(ellipse at 50% 60%, rgba(230,160,90,.5), transparent 70%),
      linear-gradient(180deg, #0e0905 0%, var(--wood-dark) 16%, var(--wood-mid) 50%, var(--wood-light) 100%);
  }
  .flourish { position: absolute; left: 0; top: 0; }
  .title {
    position: absolute; top: 10px; left: 0; right: 0; text-align: center;
    font-family: "Pinyon Script", cursive; font-weight: 400; font-size: 31px;
    color: var(--peach);
  }
  .details {
    position: absolute; left: 26px; top: 92px; list-style: none;
    font-family: "Pinyon Script", cursive; font-size: 27px; line-height: 36px;
    color: var(--peach);
    text-shadow: 0 0 .4px var(--peach);
  }
  .portrait {
    position: absolute; top: 316px; width: 112px; height: 166px;
    border-radius: 50% / 46%;
    background: radial-gradient(ellipse at 50% 45%, #d6d3cf 0%, #8f8b87 55%, rgba(40,38,36,0) 78%);
  }
  .portrait--calloway { left: 22px; }
  .portrait--dunmore { left: 158px; }
  .portrait--vostell { left: 290px; }
  .portrait--hargrove { left: 428px; }
  .partners {
    position: absolute; left: 18px; right: 18px; top: 510px;
    display: flex; justify-content: space-between;
    font-family: "Sorts Mill Goudy", serif; font-size: 14px;
    color: var(--peach);
  }
  .partner { display: flex; align-items: center; gap: 8px; }
  .partner__mark { width: 14px; height: 14px; background: var(--peach); }
  .offer {
    position: absolute; left: 18px; width: 515px; top: 606px;
    font-family: "Cormorant Garamond", serif; font-weight: 700;
    font-size: 21.5px; line-height: 23px;
    color: var(--ink);
  }
  .more-info {
    position: absolute; left: 18px; top: 708px;
    font-family: "Sorts Mill Goudy", serif; font-size: 13px;
    color: var(--ink);
  }
</style>
</head>
<body>
  <main class="poster">
    <div class="building" role="img" aria-label="Dim photograph of a Gothic college building"></div>
    <div class="score" role="img" aria-label="Faint sheet music overlay"></div>
    <div class="floor" role="img" aria-label="Warm-lit polished wooden stage floor"></div>
    <svg class="flourish" width="561" height="90" viewBox="0 0 561 90" aria-hidden="true">
      <path d="M140 5 C150 40 200 55 280 58 C360 60 420 52 470 38" fill="none" stroke="var(--peach-deep)" stroke-width="1.2" opacity=".8"/>
    </svg>
    <h1 class="title">St Wendelin's Day</h1>
    <ul class="details">
      <li>22nd November 2013, 8pm</li>
      <li>Radley Hall Oratory, Oxford</li>
      <li>Choir of St Oswin by the Tanner Row</li>
      <li>Giles Pemberton-Roe, director</li>
      <li>Tickets: £5 [from Passgrabber.example – to be set up]</li>
    </ul>
    <div class="portrait portrait--calloway" role="img" aria-label="Black and white portrait of Rupert Calloway"></div>
    <div class="portrait portrait--dunmore" role="img" aria-label="Black and white portrait of R. P. Dunmore"></div>
    <div class="portrait portrait--vostell" role="img" aria-label="Black and white portrait of Peregrine Vostell"></div>
    <div class="portrait portrait--hargrove" role="img" aria-label="Black and white portrait of Walter P. Hargrove"></div>
    <div class="partners">
      <span class="partner"><span class="partner__mark"></span>St Oswin by the Tanner Row</span>
      <span class="partner"><span class="partner__mark"></span>Passgrabber.example</span>
    </div>
    <p class="offer">Concert-goers will be able to buy the choir's latest 5-star reviewed CD "The Ashcombe Legacy" for just £8 (R.R.P. £12.95).</p>
    <p class="more-info">[More information: www.gilespembertonroe.example and www.oswin-choir.example]</p>
  </main>
</body>
</html>
```